It's a new electrical company based in Newcastle NSW. I would like a logo between the two words "BRYN (insert logo) VOLT". I would like the logo to represent electrical and celtic style. For example I have seen a light bulb with a celtic pattern in the middle which looked very good. I would like it to be a white card, mainly black writing and quite basic not too much going on. But maybe have the logo partially red or green?

BRYN VOLT
Electrical Contractors
Domestic, commercial, fault finding, testing, re wires, switchboard upgrades
License No: 738421K
Fully Insured
Phone: 0431587720

```html
<!DOCTYPE html>
<html lang="en">
<head>
<meta charset="utf-8">
<title>Bryn Volt – Business Card Proofs</title>
<link rel="stylesheet" href="https://fonts.googleapis.com/css2?family=Abril+Fatface&family=Alegreya:wght@700&family=Libre+Baskerville:wght@700&family=Sorts+Mill+Goudy&display=swap">
<style>
  :root {
    --sheet-yellow: #fff97a;
    --card-white: #ffffff;
    --ink: #1a1a1a;
    --edge: #555555;
    --accent-red: #d9261c;
  }
  html, body {
    margin: 0;
    padding: 0;
    width: 1079px;
    height: 1200px;
    overflow: hidden;
    background: var(--card-white);
  }
  .canvas {
    position: relative;
    width: 1079px;
    height: 1200px;
  }
  .sheet {
    position: absolute;
    left: 0; top: 0;
    width: 857px; height: 1180px;
    background: var(--sheet-yellow);
    border: 1px solid var(--edge);
    box-sizing: border-box;
  }
  .card {
    position: absolute;
    background: var(--card-white);
    border: 1px solid var(--edge);
    box-sizing: border-box;
    color: var(--ink);
    overflow: hidden;
  }
  .card--full { left: 99px; top: 127px; width: 654px; height: 452px; }
  .card--simple { left: 102px; top: 608px; width: 654px; height: 453px; }

  .line {
    position: absolute;
    left: 0; width: 100%;
    text-align: center;
    white-space: nowrap;
    margin: 0;
  }
  .services {
    top: 26px;
    font-family: "Sorts Mill Goudy", serif;
    font-size: 34px;
  }
  .brand-mark {
    position: absolute;
    left: 24px; top: 104px;
    width: 160px; height: 160px;
    border-radius: 50%;
    background: var(--accent-red);
  }
  .brand-name {
    position: absolute;
    font-family: "Abril Fatface", serif;
    font-weight: 400;
    transform-origin: left top;
    white-space: nowrap;
    margin: 0;
    line-height: 1;
  }
  .card--full .brand-name { left: 208px; top: 94px; font-size: 130px; transform: scaleX(0.57); }
  .card--simple .brand-name { left: 84px; top: 99px; font-size: 160px; transform: scaleX(0.59); }

  .rule {
    position: absolute;
    height: 5px;
    background: var(--ink);
  }
  .card--full .rule { left: 251px; top: 250px; width: 347px; }
  .card--simple .rule { left: 135px; top: 292px; width: 440px; }

  .detail {
    font-family: "Alegreya", serif;
    font-weight: 700;
    font-size: 41px;
    font-variant-numeric: lining-nums;
  }
  .detail--licence { top: 286px; }
  .detail--phone { top: 340px; }

  .town {
    text-decoration: underline;
  }
  .card--full .town {
    top: 392px;
    font-family: "Libre Baskerville", serif;
    font-weight: 700;
    font-size: 34px;
    text-decoration-thickness: 3px;
    text-underline-offset: 6px;
  }
  .card--simple .town {
    top: 296px;
    font-family: "Sorts Mill Goudy", serif;
    font-weight: 400;
    font-size: 84px;
    line-height: 1.2;
    transform: scaleX(0.8);
    transform-origin: center top;
    text-decoration-thickness: 4px;
    text-underline-offset: 10px;
  }
  .stray-note {
    position: absolute;
    left: 760px; top: 777px;
    font-family: "Sorts Mill Goudy", serif;
    font-size: 14px;
    color: var(--card-white);
    width: 97px;
    overflow: hidden;
    white-space: nowrap;
  }
</style>
</head>
<body>
<div class="canvas">
  <div class="sheet">
    <section class="card card--full">
      <p class="line services">Electrical Contractors Domsstic, comercial</p>
      <div class="brand-mark" aria-hidden="true"></div>
      <h1 class="brand-name">”Bryn Volt”</h1>
      <div class="rule"></div>
      <p class="line detail detail--licence">Switchboard Lisensi No: 738421K</p>
      <p class="line detail detail--phone">Full Insured Phone: 0431587720</p>
      <p class="line town">New Cestle</p>
    </section>

    <section class="card card--simple">
      <h2 class="brand-name">”Bryn Volt”</h2>
      <div class="rule"></div>
      <p class="line town">New Cestle</p>
    </section>

    <span class="stray-note">Full Insured</span>
  </div>
</div>
</body>
</html>
```